Business card design for Velvet Harbor

We need business cards designed for our new marketing consulting company, Velvet Harbor. Our services include marketing strategy, go-to-market and launch planning, growth strategy, and execution. We serve medical technology and health technology companies, from startups to well-established growth companies.

The business cards should feel professional, credible, reliable and trustworthy, and should instill confidence. Also bold, creative, and modern.

The design must use the Velvet Harbor logo.

The primary brand color is this orange: #FF5501
A secondary color that you can use is this gray: #282B2D
I would prefer only to use the orange and gray. But if you feel you really need an additional accent color (please use it very sparingly, as little as possible), you can use this blue for small accent purposes: #009FED

Attached are the logo files. The main logo is the one with a little bit of orange on the left and the rest is gray.

The business card should include the following:

Velvet Harbor logo
First name and last name
Title
Email address
Phone number and type (in whatever order looks best for the design
Website (the website does not need to be in the same block as the personal info)

For example:

Nessa Pryle
Founder & Principal
nessa@velvetharbor.com
+1.628.309.4156 mobile (can use "." or spaces in between blocks of numbers)
velvetharbor.com (somewhere on the card, it does not need to be with the personal info; and note that there is no "www." at the beginning)

Note that there will be no address listed on the business card.

Target Market(s)

Executives (CEO, head of marketing, head of sales) at medical technology and health technology companies, mostly in their 40s and older, well-educated, often with advanced degrees. They are strategic thinkers, responsible for budgets, and familiar with P&L. Their comfort with and trust in using outside consultants varies.

Industry/Entity Type

Medical technology and health technology companies.

Contact Information for Business Card

See project description

Font styles to use
Sans Serif

Requirements
Must have
• Logo and see Business card details section above.

```html
<!DOCTYPE html>
<html lang="en">
<head>
<meta charset="utf-8">
<title>Velvet Harbor — Business Card</title>
<link rel="stylesheet" href="https://fonts.googleapis.com/css2?family=Poppins:wght@300;400;700&display=swap">
<style>
  :root {
    --stage: #222222;
    --orange: #f15a24;
    --gray: #272a2c;
    --white: #ffffff;
    --muted: #e9e9e9;
    --rule: #8a8d90;
  }
  * { box-sizing: border-box; margin: 0; padding: 0; }
  html, body { width: 1200px; height: 711px; overflow: hidden; }
  body {
    background: var(--stage);
    font-family: "Poppins", Arial, sans-serif;
    display: flex;
    align-items: center;
    justify-content: center;
    gap: 40px;
  }
  .card {
    position: relative;
    width: 540px;
    height: 310px;
    border-radius: 22px;
    overflow: hidden;
    box-shadow: 0 10px 24px rgba(0,0,0,.45);
  }
  /* Back */
  .card-back { background: var(--orange); }
  .card-back .pattern-area { position: absolute; inset: 0; background: var(--orange); }
  .card-back .brand {
    position: absolute; right: 44px; bottom: 70px;
    display: flex; align-items: center; gap: 10px;
    color: var(--white);
  }
  .brand-dot {
    width: 20px; height: 20px; border-radius: 50%;
    border: 3px solid currentColor;
    flex: none;
  }
  .brand-name {
    font-weight: 400; letter-spacing: .22em; text-transform: uppercase;
    line-height: 1.05;
  }
  .card-back .brand-name { font-size: 11px; }
  /* Front */
  .card-front { background: var(--gray); color: var(--white); }
  .wave { position: absolute; inset: 0; width: 100%; height: 100%; }
  .front-brand {
    position: absolute; left: 40px; top: 96px;
    display: flex; align-items: center; gap: 14px;
  }
  .front-brand .brand-dot { width: 40px; height: 40px; border-width: 5px; }
  .front-brand .brand-name { font-size: 21px; letter-spacing: .24em; }
  .divider {
    position: absolute; left: 262px; top: 34px;
    width: 1px; height: 120px; background: var(--rule);
  }
  .person { position: absolute; left: 290px; top: 34px; }
  .person-name { font-size: 25px; line-height: 1.1; font-weight: 400; }
  .person-name .first { color: var(--orange); font-weight: 700; }
  .person-title { font-size: 11.5px; font-weight: 300; color: var(--muted); margin-top: 2px; }
  .contacts { list-style: none; margin-top: 18px; font-size: 12px; font-weight: 300; }
  .contacts li { display: flex; align-items: center; gap: 10px; margin-bottom: 6px; }
  .contacts svg { width: 12px; height: 12px; fill: var(--orange); flex: none; }
  .website {
    position: absolute; left: 270px; bottom: 28px;
    font-size: 14px; font-weight: 300; color: var(--white); letter-spacing: .02em;
  }
</style>
</head>
<body>
  <section class="card card-back" aria-label="Card back">
    <div class="pattern-area" role="img" aria-label="Repeating brand-mark pattern on orange"></div>
    <div class="brand">
      <span class="brand-dot"></span>
      <span class="brand-name">Velvet<br>Harbor</span>
    </div>
  </section>

  <section class="card card-front" aria-label="Card front">
    <svg class="wave" viewBox="0 0 540 310" preserveAspectRatio="none" aria-hidden="true">
      <path fill="var(--orange)" d="M0,272 C120,215 260,215 400,197 C480,186 525,162 540,112 L540,310 L0,310 Z"/>
      <path fill="var(--white)" d="M40,250 C130,202 260,202 390,184 C470,173 515,148 526,102 C520,144 480,182 400,194 C260,214 130,212 40,250 Z"/>
    </svg>

    <div class="front-brand">
      <span class="brand-dot"></span>
      <span class="brand-name">Velvet<br>Harbor</span>
    </div>

    <div class="divider"></div>

    <div class="person">
      <h1 class="person-name"><span class="first">Nessa</span> Pryle</h1>
      <p class="person-title">Founder &amp; Principal</p>
      <ul class="contacts">
        <li>
          <svg viewBox="0 0 24 24"><path d="M6.6 10.8a15.1 15.1 0 0 0 6.6 6.6l2.2-2.2a1 1 0 0 1 1-.25 11.4 11.4 0 0 0 3.6.57 1 1 0 0 1 1 1V20a1 1 0 0 1-1 1A17 17 0 0 1 3 4a1 1 0 0 1 1-1h3.5a1 1 0 0 1 1 1c0 1.25.2 2.45.57 3.57a1 1 0 0 1-.25 1z"/></svg>
          <span>+1.628.309.4156</span>
        </li>
        <li>
          <svg viewBox="0 0 24 24"><path d="M2 5h20v14H2zm2 2v.5l8 5 8-5V7zm0 2.9V17h16V9.9l-8 5z"/></svg>
          <span>nessa@velvetharbor.com</span>
        </li>
      </ul>
    </div>

    <p class="website">velvetharbor.com</p>
  </section>
</body>
</html>
```